someone who can choose good colours and fonts and a style for an already layed out web page

HI

We need someone who can choose good colors and fonts and style for an already layed out web page.

please look at the first file.

The hard part of what needs to go where is already done,

1) we just need a type of character suitable for our business

2) colors probably in the green / yellow spectrum to suit our business

3) we need you to choose the style. For example you could choose round photos, or square buttons, video boxes with or without frames, that sort of stuff, just tweaking of what is there. plain arial is probably what we'd like but with text but with script or memorable headings. We would just like a design style that you think would be good gor our business model.

4) the twitter,facebook logo needs to be put in a new place

our project is an Italian style village in Italy called "Casale Delle Ginestre", in Abruzzo, Italy.
It is surrounded by vineyards, lake and olive trees.

The most important is that it looks expensive, the village is eco friendly so anything on those lines is great, Obviously Italian, so italian looking characters

our website is www.collinaserena.example but we are updating it. we like the style of the old site , but it is too out of date

you can create the layout using the files we've given below and boxes
Updates

hi we've just updated out brief to make it more simple, its actually not much work its just about design choices

Target Market(s)

all lovers of Italian things
eco frienly

Industry/Entity Type

Business

Font styles to use
Decorative
Script

Colors
fcf9ce
faee3f
fde18a
fece3e
cadf82
9bcb3b
acd036
fce7d2
ec2027

Requirements
Must have
• has to have the same layout or similar so as all the boxes and links are in there
twitter,facebook and other logos need to be present where you want them
Nice to have
• we have chosen some colors but you can choose others 3 or 4 are usual a good number with a light yellow background maybe....
Should not have
• no old style must look up to date

```html
<!DOCTYPE html>
<html lang="en">
<head>
<meta charset="utf-8">
<title>Casale Delle Ginestre</title>
<link rel="stylesheet" href="https://fonts.googleapis.com/css2?family=Courgette&family=Parisienne&family=Gelasio:ital,wght@0,400;0,700;1,700&family=Source+Sans+3:wght@400;600&display=swap">
<style>
:root{
  --cream:#fdfcd2;
  --green:#6c9a1f;
  --green-dark:#557a15;
  --btn:#7aa32a;
  --ink:#1e1e1e;
  --muted:#8a8a8a;
  --line:#c9c9c9;
  --footer:#333333;
  --leaf:#9bcb3b;
}
*{box-sizing:border-box;margin:0;padding:0}
html,body{width:1200px;height:2229px;overflow:hidden;background:#fff}
body{position:relative;font-family:"Gelasio",Georgia,serif;color:var(--ink)}
.abs{position:absolute}

/* header */
.site-header{left:0;top:0;width:1200px;height:163px;background:var(--cream)}
.brand-mark{left:22px;top:22px;width:100px;height:100px;border-radius:50%;background:var(--green)}
.brand-name{left:0;top:30px;width:1200px;text-align:center;font-family:"Parisienne",cursive;font-size:64px;color:#3a3a2a}
.contact-line{left:955px;font-family:"Source Sans 3",Arial,sans-serif;font-size:16px;color:#222;display:flex;align-items:center;gap:10px;white-space:nowrap}
.flags{left:955px;top:125px;display:flex;gap:14px}
.flag{width:22px;height:14px;display:flex}
.flag span{flex:1}

/* nav */
.main-nav{left:0;top:166px;width:1200px;height:90px}
.main-nav .bar{left:320px;top:0;width:116px;height:6px;background:var(--green)}
.nav-item{top:36px;font-family:"Source Sans 3",Arial,sans-serif;font-size:21px;color:#222;display:flex;align-items:center;gap:9px;white-space:nowrap}
.nav-item.active{color:var(--green);font-weight:600}
.caret{width:0;height:0;border-left:5px solid transparent;border-right:5px solid transparent;border-top:6px solid currentColor}

/* hero */
.collage{left:34px;top:257px;width:527px;height:562px;background:#fdfbe3}
.thumb{top:2px;width:96px;height:92px}
.thumb-cap{top:98px;width:104px;font-family:"Source Sans 3",Arial,sans-serif;font-size:12px;line-height:14px;color:#222;white-space:nowrap}
.site-plan{left:0;top:118px;width:527px;height:444px;background:linear-gradient(160deg,#eef0c8,#a9cc63 45%,#6ea13a 80%,#f1efd0)}
.slider{left:600px;top:257px;width:569px;height:562px;background:linear-gradient(180deg,#8fb5e0 0%,#a7c2dd 25%,#7a5a4a 45%,#4e6b34 62%,#4f8a26 100%)}
.slide-caption{left:154px;top:351px;width:389px;height:95px;background:rgba(240,240,235,.55);font-family:"Parisienne",cursive;font-size:31px;color:#fff;display:flex;align-items:center;justify-content:center;white-space:nowrap}
.slide-thumbs{left:0;top:463px;width:569px;height:99px;background:#6f9a3a}
.slide-thumb{top:12px;width:86px;height:80px;border:3px solid #fff}
.arrow{top:45px;width:0;height:0;border-top:7px solid transparent;border-bottom:7px solid transparent}

/* intro */
.intro{left:55px;top:858px;width:1092px;font-family:"Courgette",cursive;font-size:18px;line-height:29px;color:var(--ink)}
.intro p{margin-bottom:29px}
.intro .lead{font-size:29px;color:var(--green);font-weight:700}
.intro em{font-style:normal;color:var(--green)}

.rule{height:1px;background:var(--line)}

/* columns */
.col-title{top:1282px;font-family:"Gelasio",Georgia,serif;font-size:37px;color:var(--green);text-align:center}
.divider{top:1294px;width:1px;height:360px;background:var(--line)}
.label{font-size:16px;color:#222;white-space:nowrap}
.field{height:31px;border:1px solid #888;background:#fff}
.btn{height:33px;background:var(--btn);color:#fff;font-family:"Gelasio",Georgia,serif;font-size:16px;display:flex;align-items:center;justify-content:center}
.date{font-size:14px;color:#999;padding-left:6px;display:flex;align-items:center;justify-content:space-between;padding-right:8px}
.cal{width:14px;height:14px;border:2px solid #555;border-top-width:4px}
.select{display:flex;align-items:center;justify-content:space-between;padding:0 8px;font-size:14px}
.season{width:116px;height:154px;border-radius:48px}
.season-name{width:116px;top:10px;text-align:center;font-family:"Gelasio",Georgia,serif;font-style:italic;font-weight:700;font-size:14px;color:#fff;letter-spacing:.5px}

/* blogs & videos */
.section-title{top:1742px;font-family:"Gelasio",Georgia,serif;font-size:29px;color:#555}
.post{left:60px;font-size:19px;color:#222;white-space:nowrap}
.video-title{font-size:16px;font-weight:700;color:#222}
.video-sub{font-size:16px;color:var(--muted);white-space:nowrap}
.video{top:1820px;width:158px;height:139px;background:linear-gradient(180deg,#5d5d5d 0%,#8d8f7a 40%,#3f3f30 100%);border:2px solid #444}
.play{left:66px;top:57px;width:0;height:0;border-top:12px solid transparent;border-bottom:12px solid transparent;border-left:18px solid #fff}

/* footer */
.site-footer{left:0;top:2031px;width:1200px;height:198px;background:var(--footer)}
.foot-col{top:22px;font-family:"Gelasio",Georgia,serif}
.foot-col h4{font-size:18px;font-weight:400;color:var(--leaf);margin-bottom:2px}
.foot-col li{list-style:none;font-size:14px;line-height:18px;color:var(--leaf)}
.foot-col li.current{color:#fff}
.foot-col li.current span{font-style:italic;font-weight:700;text-decoration:underline}
.social{left:985px;width:26px;height:26px;border-radius:50%;background:var(--leaf)}
.copyright{left:0;top:169px;width:1200px;text-align:center;font-size:12px;line-height:14px;color:#fff}
</style>
</head>
<body>

<header class="abs site-header">
  <div class="abs brand-mark" role="img" aria-label="Casale Delle Ginestre emblem"></div>
  <div class="abs brand-name">Casale Delle Ginestre</div>
  <div class="abs contact-line" style="top:14px">
    <svg width="28" height="26" viewBox="0 0 28 26" aria-hidden="true"><rect x="2" y="8" width="24" height="16" rx="3" fill="none" stroke="#222" stroke-width="2"/><path d="M5 9 Q14 0 23 9" fill="none" stroke="#222" stroke-width="3"/><circle cx="14" cy="16" r="4" fill="none" stroke="#222" stroke-width="2"/></svg>
    <span>0850000123</span>
  </div>
  <div class="abs contact-line" style="top:60px">
    <svg width="28" height="22" viewBox="0 0 28 22" aria-hidden="true"><rect x="1" y="1" width="26" height="20" fill="none" stroke="#222" stroke-width="2"/><path d="M1 1 L14 12 L27 1" fill="none" stroke="#222" stroke-width="2"/></svg>
    <span>Via dei Pini 12, Colleverde</span>
  </div>
  <div class="abs flags" aria-label="Languages">
    <div class="flag"><span style="background:#2a9a3a"></span><span style="background:#fff"></span><span style="background:#d42a2a"></span></div>
    <div class="flag" style="background:#24367a"><span></span></div>
    <div class="flag" style="flex-direction:column"><span style="background:#111"></span><span style="background:#d01d1d"></span><span style="background:#f2c200"></span></div>
  </div>
</header>

<nav class="abs main-nav">
  <div class="abs bar"></div>
  <div class="abs nav-item active" style="left:320px">Description <i class="caret"></i></div>
  <div class="abs nav-item" style="left:478px">Which Reason <i class="caret"></i></div>
  <div class="abs nav-item" style="left:680px">PriceList <i class="caret"></i></div>
  <div class="abs nav-item" style="left:800px">Contact Us</div>
</nav>

<section class="abs collage">
  <div class="abs thumb" role="img" aria-label="Sunflower in the sun" style="left:2px;background:linear-gradient(#4a8a3a,#f2c420)"></div>
  <div class="abs thumb" role="img" aria-label="Child playing on the beach" style="left:108px;background:linear-gradient(#f0d9a0,#c89a5a)"></div>
  <div class="abs thumb" role="img" aria-label="Snowy mountain slope" style="left:214px;background:linear-gradient(#3f5fa8,#e8e8f0)"></div>
  <div class="abs thumb" role="img" aria-label="Olive grove" style="left:320px;background:linear-gradient(#c7d9a0,#5a7a3a)"></div>
  <div class="abs thumb" role="img" aria-label="Colosseum in Rome" style="left:426px;background:linear-gradient(#6aa0e0,#b58a50)"></div>
  <div class="abs thumb-cap" style="left:10px">In the sun</div>
  <div class="abs thumb-cap" style="left:115px">By the beach</div>
  <div class="abs thumb-cap" style="left:214px">Ski in mountains</div>
  <div class="abs thumb-cap" style="left:318px">BBQ in olive grove</div>
  <div class="abs thumb-cap" style="left:432px">Near Rome</div>
  <div class="abs site-plan" role="img" aria-label="Illustrated site plan of the village phases, gardens, lake and playground"></div>
</section>

<section class="abs slider" role="img" aria-label="Villa courtyard with landscaped lawn">
  <div class="abs slide-caption">Refreshing Landscaped Gardens</div>
  <div class="abs slide-thumbs">
    <div class="abs arrow" style="left:4px;border-right:9px solid #fff"></div>
    <div class="abs slide-thumb" style="left:24px;background:linear-gradient(#8aa8c8,#4f7a30)"></div>
    <div class="abs slide-thumb" style="left:136px;background:linear-gradient(#a0b8d8,#e8ecf2)"></div>
    <div class="abs slide-thumb" style="left:248px;background:linear-gradient(#d8c8a8,#7a6a4a)"></div>
    <div class="abs slide-thumb" style="left:360px;background:linear-gradient(#3f5a2a,#a07040)"></div>
    <div class="abs slide-thumb" style="left:460px;background:linear-gradient(#b0c8e0,#9aa080)"></div>
    <div class="abs arrow" style="left:556px;border-left:9px solid #fff"></div>
  </div>
</section>

<section class="abs intro">
  <p><span class="lead">Casale Delle Ginestre</span> is built in traditional Italian architectural style and surrounded by olive groves, vineyards, a beautiful lake surrounded by a park with wildlife. The panoramic view of the mountains is breathtaking and you can see for 30 miles on a clear day. <em>Red and white umbrellas</em>, <em>barbeques</em>, <em>swimming pools</em> and a <em>spa</em> will contribute to its unique atmosphere. there will also be a health farm, where you can treat yourself to a <em>luxurious massage</em>.</p>
  <p>Ten shops and ensure any of your other needs can be met. Casale Delle Ginestre is ensconced in the beauty of the Italian countryside, where the hot white sandy beaches of the <em>Adriatic coastline meet the cold snowy ski-slopes of the Appenine mountains</em>, with Rome only a short car ride away.</p>
  <p>Each property will be in the <em>OLD Abruzzo style</em>, with attractive brick and stone walls. There are one-, two- and three-bedroomed apartments and three- or four-bedroomed villas.</p>
</section>

<div class="abs rule" style="left:55px;top:1265px;width:1082px"></div>

<!-- newsletter -->
<div class="abs col-title" style="left:55px;width:290px">NEWSLETTER</div>
<div class="abs label" style="left:55px;top:1352px;font-size:20px">Sign Up for Our NewsLetter</div>
<div class="abs label" style="left:57px;top:1405px">Name</div>
<div class="abs field" style="left:57px;top:1440px;width:274px"></div>
<div class="abs label" style="left:57px;top:1497px">Email</div>
<div class="abs field" style="left:57px;top:1532px;width:274px"></div>
<div class="abs btn" style="left:58px;top:1618px;width:124px">Submit</div>

<div class="abs divider" style="left:394px"></div>

<!-- seasons -->
<div class="abs col-title" style="left:394px;width:374px">SEASONS</div>
<div class="abs season" role="img" aria-label="Spring meadow with poppies" style="left:442px;top:1354px;background:linear-gradient(#9aa86a,#5a8a2a 60%,#a03a20)"><div class="abs season-name">SPRING</div></div>
<div class="abs season" role="img" aria-label="Autumn hills" style="left:591px;top:1354px;background:linear-gradient(#a8c0d8,#6a6a3a 50%,#8a5a30)"><div class="abs season-name">AUTUMN</div></div>
<div class="abs season" role="img" aria-label="Winter mountains" style="left:442px;top:1515px;background:linear-gradient(#d0d8e0,#6a7a6a 55%,#2f3a2a)"><div class="abs season-name">WINTER</div></div>
<div class="abs season" role="img" aria-label="Summer vineyard" style="left:591px;top:1515px;background:linear-gradient(#c8e0f0,#6a8a3a 45%,#3a5a1a)"><div class="abs season-name">SUMMER</div></div>
<div class="abs" style="left:394px;top:1673px;width:374px;text-align:center;font-size:15px;font-family:'Source Sans 3',Arial,sans-serif"><span style="color:var(--green);font-weight:600;text-decoration:underline">CLICK HERE</span> for More photos</div>

<div class="abs divider" style="left:768px"></div>

<!-- book trip -->
<div class="abs col-title" style="left:768px;width:412px">BOOK TRIP</div>
<div class="abs label" style="left:799px;top:1368px">Name</div>
<div class="abs field" style="left:931px;top:1363px;width:217px"></div>
<div class="abs label" style="left:799px;top:1408px">Check-In Date</div>
<div class="abs field date" style="left:931px;top:1402px;width:217px">mm/dd/yyyy<i class="cal"></i></div>
<div class="abs label" style="left:799px;top:1448px">Check-Out Date</div>
<div class="abs field date" style="left:931px;top:1442px;width:217px">mm/dd/yyyy<i class="cal"></i></div>
<div class="abs label" style="left:799px;top:1486px">No. Of Persons</div>
<div class="abs label" style="left:878px;top:1512px;font-size:14px">Adult</div>
<div class="abs field select" style="left:926px;top:1508px;width:61px;height:30px">1<i class="caret"></i></div>
<div class="abs label" style="left:1018px;top:1512px;font-size:14px">Children</div>
<div class="abs field select" style="left:1090px;top:1508px;width:57px;height:30px">0<i class="caret"></i></div>
<div class="abs label" style="left:799px;top:1561px">Email</div>
<div class="abs field" style="left:931px;top:1556px;width:217px"></div>
<div class="abs btn" style="left:898px;top:1618px;width:124px">BOOK NOW</div>

<div class="abs rule" style="left:55px;top:1706px;width:1082px"></div>

<!-- blogs -->
<div class="abs section-title" style="left:60px">BLOGS</div>
<div class="abs post" style="top:1810px">Post 1 : Why should we retire in Italy? .... (2 comments)</div>
<div class="abs post" style="top:1860px">Post 2: Information for US Citizens .... (5 comments)</div>
<div class="abs post" style="top:1910px">Post 3: Lorem ipsum dolor sit amet. dolor sit .... (0 comments)</div>
<div class="abs" style="left:463px;top:1954px;font-size:16px;color:var(--green)">Read More &gt;&gt;</div>
<div class="abs btn" style="left:57px;top:1976px;width:176px;height:31px;font-size:15px">Browse Older Posts</div>

<!-- videos -->
<div class="abs section-title" style="left:727px">VIDEOS</div>
<div class="abs video-title" style="left:730px;top:1778px">Video 1</div>
<div class="abs video-sub" style="left:730px;top:1797px">Abruzzo Borgo Nov. 2010</div>
<div class="abs video" role="img" aria-label="Video preview of hillside landscape" style="left:730px"><div class="abs play"></div></div>
<div class="abs video-title" style="left:962px;top:1778px">Video 2</div>
<div class="abs video-sub" style="left:962px;top:1797px">Olive Harvest Nov. 2010</div>
<div class="abs video" role="img" aria-label="Video preview of olive harvest" style="left:962px"><div class="abs play"></div></div>

<footer class="abs site-footer">
  <div class="abs foot-col" style="left:285px">
    <h4>Description</h4>
    <ul><li class="current">- <span>Home</span></li><li>- Styles</li><li>- Alanno</li><li>- Places NearBy</li><li>- Casale Shops</li><li>- Phases</li></ul>
  </div>
  <div class="abs foot-col" style="left:465px">
    <h4>Which Reason?</h4>
    <ul><li>- Reasons</li><li>- Motives</li></ul>
  </div>
  <div class="abs foot-col" style="left:645px">
    <h4>Prices</h4>
    <ul><li>- Buying Procedure</li><li>- Price List</li><li>- Mortgage</li></ul>
  </div>
  <div class="abs foot-col" style="left:825px">
    <h4>Contact Us</h4>
  </div>
  <div class="abs social" role="img" aria-label="Social page link" style="top:48px"></div>
  <div class="abs social" role="img" aria-label="Social feed link" style="top:97px"></div>
  <div class="abs social" role="img" aria-label="Video channel link" style="top:142px"></div>
  <div class="abs copyright">(c) 2013 Casale Delle Ginestre - CasaCollina Italia S.r.L.<br>More properties for sale in Abruzzo, Case Collina Italia</div>
</footer>

</body>
</html>
```